Custom unique Stationary design for Logistics company

We need a custom, unique , elegant and luxurious full stationary design using our new logo, following these guidelines:
1- Business card: double sided, both sides uses the navy blue as the background main color (same as the code of the navy blue used in our logo).
2- envelope and folder: also use the same navy blue as the main background color.
3- book cover( notepad cover) : same thing with the navy blue
4- letterhead: feel free to use the combination of the colors in our logo.
5- rest of the items are up to your creativity

Target Market(s)

corporates and other businesses

Industry/Entity Type

Logistics and heavy machines contractors

Requirements
Must have
• Letterhead, business card, envelope, notepad cover, paper, file
Nice to have
• navy blue to be main background color for business card, envelope, notepad cover

```html
<!DOCTYPE html>
<html lang="en">
<head>
<meta charset="utf-8">
<title>Northgate Freight Group – Letterhead</title>
<link href="https://fonts.googleapis.com/css2?family=Open+Sans:wght@600;700&display=swap" rel="stylesheet">
<style>
  :root {
    --navy: #004d71;
    --orange: #ee6a3c;
    --rule-grey: #c7c7c7;
    --ink-grey: #6b6b6b;
    --paper: #ffffff;
    --backdrop: #a9cdef;
  }
  * { margin: 0; padding: 0; box-sizing: border-box; }
  html, body {
    width: 1200px; height: 784px; overflow: hidden;
    background: var(--backdrop);
    font-family: "Open Sans", sans-serif;
  }
  .letterhead {
    position: absolute; left: 338px; top: 22px;
    width: 524px; height: 740px;
    background: var(--paper);
    box-shadow: 0 2px 10px rgba(0, 40, 80, 0.15);
    overflow: hidden;
  }
  .letterhead__header {
    position: absolute; left: 0; top: 0; width: 100%; height: 72px;
    background: var(--navy);
    display: flex; align-items: center; justify-content: center;
  }
  .letterhead__rule {
    position: absolute; left: 0; top: 74px; width: 100%; height: 3px;
    background: var(--rule-grey);
  }
  .brand {
    display: flex; align-items: center; gap: 7px;
    color: #fff; font-weight: 700; font-size: 15px; letter-spacing: 1.5px;
    text-transform: uppercase;
  }
  .brand__dot {
    width: 9px; height: 9px; border-radius: 50%; background: var(--orange);
  }
  .letterhead__footer {
    position: absolute; left: 0; bottom: 0; width: 100%; height: 52px;
  }
  .footer-art { position: absolute; left: 0; top: 0; }
  .contact-line {
    position: absolute; left: 10px; top: 6px;
    display: flex; align-items: center; gap: 6px;
    font-size: 7px; font-weight: 700; color: var(--ink-grey);
    white-space: nowrap;
  }
  .contact-line__item { display: flex; align-items: center; gap: 3px; }
  .contact-line__icon { width: 8px; height: 8px; }
  .website {
    position: absolute; right: 14px; bottom: 13px;
    font-size: 8px; font-weight: 700; color: #fff;
  }
</style>
</head>
<body>
  <main class="letterhead">
    <header class="letterhead__header">
      <div class="brand"><span class="brand__dot"></span>Northgate Freight Group</div>
    </header>
    <div class="letterhead__rule"></div>

    <footer class="letterhead__footer">
      <svg class="footer-art" width="524" height="52" viewBox="0 0 524 52" aria-hidden="true">
        <polygon points="0,26 112,26 108,30 0,30" fill="var(--orange)"/>
        <polygon points="116,26 244,26 240,30 112,30" fill="var(--navy)"/>
        <polygon points="248,26 372,26 368,30 244,30" fill="var(--orange)"/>
        <rect x="0" y="36" width="524" height="16" fill="var(--navy)"/>
        <polygon points="378,20 524,20 524,52 366,52" fill="var(--navy)"/>
      </svg>
      <div class="contact-line">
        <span class="contact-line__item">
          <svg class="contact-line__icon" viewBox="0 0 10 10"><circle cx="5" cy="5" r="5" fill="var(--navy)"/><path d="M5 2.2a1.8 1.8 0 0 1 1.8 1.8c0 1.3-1.8 3.6-1.8 3.6S3.2 5.3 3.2 4A1.8 1.8 0 0 1 5 2.2z" fill="#fff"/></svg>
          12 Harbor Rd, Fairview, OH 00000, United States
        </span>
        <span class="contact-line__item">
          <svg class="contact-line__icon" viewBox="0 0 10 10"><circle cx="5" cy="5" r="5" fill="var(--navy)"/><path d="M3.4 2.6l1 1-.6.7c.4.8 1 1.4 1.8 1.8l.7-.6 1 1-.6.9C4.9 7.3 2.7 5.1 2.6 3.2z" fill="#fff"/></svg>
          +10000000077
        </span>
        <span class="contact-line__item">
          <svg class="contact-line__icon" viewBox="0 0 10 10"><circle cx="5" cy="5" r="5" fill="var(--navy)"/><rect x="2.5" y="3.3" width="5" height="3.4" fill="#fff"/><path d="M2.5 3.3L5 5.2l2.5-1.9" stroke="var(--navy)" stroke-width=".6" fill="none"/></svg>
          contact@northgatefreight.com
        </span>
      </div>
      <div class="website">www.northgatefreight.com</div>
    </footer>
  </main>
</body>
</html>
```